WPC - world groomers association website

Northfield Pet Collective (WPC) is a new association located in USA, start the first project in South Korea. As now we do the following business:
1. We supply dog grooming education
2. We certify dog groomers
3. We host dog grooming education events
4. We organize grooming trade show

The design:
Because this organization is related to dog grooming, so beautiful groomed dog images are important. I will upload some well groomed dog images. I want you are able to put all these images or some of the images together either nice color or just layout of the images. I want the first page impressive. This business is related to grooming education, so I want our customers get impressed by visiting our website and decide to contact us for their continuing education. Also since this is an association, I want the website to be some level of institutional. Background layout and images catch eyes, but the content area simple and clear.

I want to be able to edit my site by adding images and edit the contents by myself in a easy way.

I need 5 pages now, but I may need to add more pages, but not more than 8 pages.

www.tavermont-sample.com is the site I really like.

Thanks.

Sans Serif

85cae6
87cfc6
cadf82
85acd3

Must have
• consistent tune on every page
Nice to have
• several well-groomed dogs, I can provide images

```html
<!DOCTYPE html>
<html lang="en">
<head>
<meta charset="utf-8">
<title>Northfield Pet Collective</title>
<link href="https://fonts.googleapis.com/css2?family=Oswald:wght@400;500&family=Open+Sans:ital,wght@0,400;0,600;0,700;1,400&display=swap" rel="stylesheet">
<style>
:root{
  --blue:#85acd3;
  --teal:#7fd1c6;
  --green:#bfd671;
  --green-text:#c5dc7e;
  --star:#7ea7d1;
  --dark:#3a3a3a;
  --darker:#333;
  --ink:#2b2b2b;
  --brand-ink:#1f3f73;
  --white:#fff;
}
*{margin:0;padding:0;box-sizing:border-box}
html,body{width:868px;height:1200px;overflow:hidden;background:#fff}
body{position:relative;font-family:"Open Sans",Arial,sans-serif;color:var(--ink)}
.abs{position:absolute}
.top-rule{left:0;top:0;width:868px;height:3px;background:var(--blue)}
.header{left:0;top:3px;width:868px;height:55px;background:#fff}
.nav{right:70px;top:22px;display:flex;gap:24px;font-family:"Oswald",sans-serif;font-size:12.5px;line-height:1;color:#333;list-style:none;align-items:center}
.nav .active{color:var(--green)}
.brand{left:63px;top:4px;width:120px;height:120px;border-radius:50%;background:#fff;z-index:3;display:flex;align-items:center;justify-content:center;text-align:center;font-family:"Oswald",sans-serif;font-size:13px;line-height:1.25;color:var(--brand-ink);padding:14px}
.hero{left:0;top:58px;width:868px;height:285px;background:linear-gradient(100deg,#9aa08c 0%,#c7c2b6 35%,#d8cdbf 60%,#ece7e3 100%)}
.hero-title{left:0;width:868px;top:180px;text-align:center;font-family:"Oswald",sans-serif;font-weight:500;font-size:38px;line-height:40px;color:#fff;letter-spacing:.5px}
.hero-sub{left:0;width:868px;top:225px;text-align:center;font-size:17px;line-height:22px;letter-spacing:6px;color:#c8de7f}
.dots{left:392px;top:321px;display:flex;gap:4px}
.dots span{width:18px;height:3px;background:#fff}
.dots span:first-child{background:var(--green)}
.feature{top:343px;height:92px;color:#fff}
.feature h3{position:absolute;left:98px;top:12px;font-family:"Oswald",sans-serif;font-weight:400;font-size:15.5px}
.feature p{position:absolute;left:98px;top:35px;width:170px;font-size:8.5px;line-height:13px;opacity:.92}
.feature a{position:absolute;left:98px;top:69px;font-size:8.5px;font-weight:700;color:var(--green-text);text-decoration:none}
.feature svg{position:absolute;left:34px;top:14px}
.welcome-title{left:0;width:868px;top:469px;text-align:center;font-family:"Oswald",sans-serif;font-weight:400;font-size:18px;color:#222}
.stars{left:398px;top:499px;display:flex;gap:5px}
.intro{left:124px;width:620px;top:525px;text-align:center;font-size:8.4px;line-height:17px;color:#666}
.card{top:594px;width:175px}
.card .photo{width:175px;height:123px}
.card h4{margin-top:17px;font-family:"Oswald",sans-serif;font-weight:400;font-size:14px;color:#222}
.card p{margin-top:8px;font-size:8.5px;line-height:15.5px;color:#777}
.card a{display:block;margin-top:7px;font-size:8.5px;font-weight:700;color:var(--green);text-decoration:none}
.testimonial{left:0;top:852px;width:868px;height:126px;background:var(--green)}
.quote-bg{left:76px;top:876px;width:80px;height:80px;border-radius:50%;background:#e3e3df}
.avatar{left:128px;top:876px;width:80px;height:80px;border-radius:50%;background:linear-gradient(160deg,#c9c9c9,#6f7a88);border:2px solid #fff}
.quote-text{left:230px;top:876px;width:560px;font-style:italic;font-size:9.9px;line-height:17.5px;color:#fff}
.quote-name{left:228px;top:940px;font-size:10.5px;font-weight:600;color:#fff}
.footer{left:0;top:978px;width:868px;height:174px;background:var(--dark)}
.col{top:1000px;color:#eee}
.col h5{font-family:"Oswald",sans-serif;font-weight:500;font-size:12.5px;color:#fff;margin-bottom:11px}
.col li{list-style:none;font-size:8.5px;line-height:15px;color:#ddd}
.divider{top:998px;width:1px;height:130px;background:#484848}
.col p{font-size:8.5px;line-height:13.5px;color:#ddd}
.email{margin-top:13px;width:194px;height:25px;background:#fff;font-size:8.5px;color:#666;padding:7px 9px}
.btn{margin-top:9px;width:67px;height:24px;background:var(--green);color:#fff;font-size:8.5px;font-weight:700;display:flex;align-items:center;justify-content:center}
.contact li{display:flex;gap:14px;align-items:flex-start;margin-bottom:8px}
.contact svg{flex:none;margin-top:2px}
.bottom{left:0;top:1152px;width:868px;height:48px;background:var(--darker)}
.copy{left:72px;top:1167px;font-size:8.5px;color:#ddd}
.social{left:692px;top:1160px;display:flex;gap:3px}
.social span{width:24px;height:24px;border-radius:50%;border:1.5px solid #fff;display:block}
</style>
</head>
<body>
<div class="abs top-rule"></div>
<header class="abs header"></header>
<div class="abs brand">Northfield Pet Collective</div>
<ul class="abs nav">
  <li class="active">HOME</li><li>ABOUT</li><li>EDUCATION</li><li>TRADE SHOWS</li><li>CERTIFICATION</li><li>EVENTS</li><li>CONTACT</li>
  <li><svg width="11" height="11" viewBox="0 0 12 12"><circle cx="5" cy="5" r="3.8" fill="none" stroke="#333" stroke-width="1.8"/><path d="M8 8l3 3" stroke="#333" stroke-width="2"/></svg></li>
</ul>

<section class="abs hero" role="img" aria-label="Photo of a small long-haired dog being brushed by a groomer"></section>
<h1 class="abs hero-title">NORTHFIELD PET COLLECTIVE</h1>
<div class="abs hero-sub">Pet Groomers Association</div>
<div class="abs dots"><span></span><span></span><span></span><span></span></div>

<div class="abs feature" style="left:0;width:288px;background:var(--blue)">
  <svg width="48" height="46" viewBox="0 0 48 46" fill="#fff"><circle cx="24" cy="10" r="8"/><circle cx="9" cy="13" r="6"/><circle cx="39" cy="13" r="6"/><path d="M10 44c0-13 6-19 14-19s14 6 14 19z"/><path d="M0 36c0-10 4-14 9-14 3 0 5 1 6 3-3 3-5 7-5 11z"/><path d="M48 36c0-10-4-14-9-14-3 0-5 1-6 3 3 3 5 7 5 11z"/></svg>
  <h3>MEMBERSHIP</h3><p>At vero eos et accusamus et iusto odio dignissimos ducimus qu</p><a>JOIN US NOW &gt;&gt;</a>
</div>
<div class="abs feature" style="left:288px;width:290px;background:var(--teal)">
  <svg width="44" height="44" viewBox="0 0 44 44"><circle cx="18" cy="18" r="13" fill="none" stroke="#fff" stroke-width="6"/><path d="M28 28l12 12" stroke="#fff" stroke-width="7" stroke-linecap="round"/></svg>
  <h3 style="left:94px">FIND A GROOMER</h3><p style="left:94px">At vero eos et accusamus et iusto odio dignissimos ducimus qu</p><a style="left:94px">FIND NOW &gt;&gt;</a>
</div>
<div class="abs feature" style="left:578px;width:290px;background:var(--blue)">
  <svg width="42" height="46" viewBox="0 0 42 46" fill="none" stroke="#fff" stroke-width="3"><rect x="2" y="7" width="38" height="37" rx="2"/><path d="M10 2v9M32 2v9M2 17h38M12 17v27M22 17v27M32 17v27M2 26h38M2 35h38"/></svg>
  <h3 style="left:97px">NEWS ARTICLES</h3><p style="left:97px">At vero eos et accusamus et iusto odio dignissimos ducimus qu</p><a style="left:97px">SEE ALL NEWS &gt;&gt;</a>
</div>

<h2 class="abs welcome-title">WELCOME TO NORTHFIELD PET COLLECTIVE</h2>
<div class="abs stars">
  <svg width="11" height="11" viewBox="0 0 10 10"><path d="M5 0l1.5 3.3 3.5.3-2.7 2.3.8 3.5L5 7.6 1.9 9.4l.8-3.5L0 3.6l3.5-.3z" fill="var(--star)"/></svg>
  <svg width="11" height="11" viewBox="0 0 10 10"><path d="M5 0l1.5 3.3 3.5.3-2.7 2.3.8 3.5L5 7.6 1.9 9.4l.8-3.5L0 3.6l3.5-.3z" fill="var(--star)"/></svg>
  <svg width="11" height="11" viewBox="0 0 10 10"><path d="M5 0l1.5 3.3 3.5.3-2.7 2.3.8 3.5L5 7.6 1.9 9.4l.8-3.5L0 3.6l3.5-.3z" fill="var(--star)"/></svg>
  <svg width="11" height="11" viewBox="0 0 10 10"><path d="M5 0l1.5 3.3 3.5.3-2.7 2.3.8 3.5L5 7.6 1.9 9.4l.8-3.5L0 3.6l3.5-.3z" fill="var(--star)"/></svg>
  <svg width="11" height="11" viewBox="0 0 10 10"><path d="M5 0l1.5 3.3 3.5.3-2.7 2.3.8 3.5L5 7.6 1.9 9.4l.8-3.5L0 3.6l3.5-.3z" fill="var(--star)"/></svg>
</div>
<p class="abs intro">At vero eos et accusamus et iusto odio dignissimos ducimus qui blanditiis praesentium voluptatum deleniti atque corrupti quos dolores et quas moles tias excepturi sint occaecati cupiditate non provident, similique sunt in culpa qui officia deserunt mollitia animi, id est laborum et dolorum fuga. Et harum quidem rerum facilis est et expedita dium soluta nobis est eligendi optio cumque nihil impedistinctio.</p>

<article class="abs card" style="left:71px">
  <div class="photo" role="img" aria-label="Photo of groomers blow-drying a golden retriever" style="background:linear-gradient(135deg,#e6e4e0,#b58a55 60%,#8a8f96)"></div>
  <h4>EDUCATION</h4><p>Nam libero tempore, cum soluta nobis est eligendi optio cumque nihil impedit quo mi nus id quod maxime placeat.</p><a>READ MORE &gt;&gt;</a>
</article>
<article class="abs card" style="left:254px">
  <div class="photo" role="img" aria-label="Photo of a dog leaping over an agility jump" style="background:linear-gradient(135deg,#4f4a46,#b07a45 50%,#6d7a5a)"></div>
  <h4>CERTIFICATION</h4><p>Nam libero tempore, cum soluta nobis est eligendi optio cumque nihil impedit quo mi nus id quod maxime placeat.</p><a>READ MORE &gt;&gt;</a>
</article>
<article class="abs card" style="left:438px">
  <div class="photo" role="img" aria-label="Photo of a golden retriever with visitors at an expo stand" style="background:linear-gradient(135deg,#c9ccd2,#d8b682 50%,#e9a43a)"></div>
  <h4>EVENTS</h4><p>Nam libero tempore, cum soluta nobis est eligendi optio cumque nihil impedit quo mi nus id quod maxime placeat.</p><a>READ MORE &gt;&gt;</a>
</article>
<article class="abs card" style="left:621px">
  <div class="photo" role="img" aria-label="Photo of an outdoor dog show crowd on a sunny field" style="background:linear-gradient(180deg,#8fb0b8,#6c6f52 45%,#8a6a48)"></div>
  <h4>TRADE SHOW</h4><p>Nam libero tempore, cum soluta nobis est eligendi optio cumque nihil impedit quo mi nus id quod maxime placeat.</p><a>READ MORE &gt;&gt;</a>
</article>

<section class="abs testimonial"></section>
<div class="abs quote-bg"><svg width="80" height="80" viewBox="0 0 80 80"><text x="10" y="62" font-family="Georgia,serif" font-size="60" fill="#c8c8c4">“</text></svg></div>
<div class="abs avatar" role="img" aria-label="Portrait photo of the quoted member"></div>
<p class="abs quote-text">It is a long established fact that a reader will be distracted by the readable content of a page when looking at its layout. The point of using Lorem Ipsum is that it has a more-or-less normal distribution of letters, as opposed to using 'Content here, content here', making it look like readable English.</p>
<div class="abs quote-name">DANA WHITFIELD</div>

<footer class="abs footer"></footer>
<div class="abs col" style="left:71px"><h5>INFORMATION</h5><ul><li>Home</li><li>About</li><li>Education</li><li>Trade Shows</li><li>Certification</li><li>Events</li><li>Contact</li></ul></div>
<div class="abs divider" style="left:170px"></div>
<div class="abs col" style="left:201px"><h5>QUICK LINKS</h5><ul><li>Membership Information</li><li>Membership Application</li><li>Find a Groomer</li><li>Member Directory</li><li>Groomer Training</li><li>Articles</li><li>Fundraising</li></ul></div>
<div class="abs divider" style="left:333px"></div>
<div class="abs col" style="left:365px"><h5>NEWSLETTER SUBSCRIPTION</h5><p>Register your email Address to get<br>information about us</p><div class="email">Email Address</div><div class="btn">SUBSCRIBE</div></div>
<div class="abs divider" style="left:588px"></div>
<div class="abs col contact" style="left:616px"><h5>CONTACT US</h5><ul>
  <li><svg width="8" height="11" viewBox="0 0 8 11"><path d="M4 0a4 4 0 0 1 4 4c0 3-4 7-4 7S0 7 0 4a4 4 0 0 1 4-4z" fill="#ddd"/><circle cx="4" cy="4" r="1.5" fill="#3a3a3a"/></svg><span style="line-height:11.5px">48 Alder Crossing, Suite 12<br>59204, Brookhaven</span></li>
  <li style="margin-top:6px"><svg width="10" height="10" viewBox="0 0 10 10"><path d="M2 0l2 2.5-1 1.3a6 6 0 0 0 3 3l1.3-1L10 8l-1.5 2C4 10 0 6 0 1.5z" fill="#ddd"/></svg>1 555 014 2290</li>
  <li style="margin-top:6px"><svg width="11" height="10" viewBox="0 0 11 10" fill="#ddd"><rect x="0" y="3" width="11" height="7" rx="1"/><rect x="2.5" y="0" width="6" height="3"/></svg>1 555 014 7731</li>
  <li style="margin-top:6px"><svg width="11" height="8" viewBox="0 0 11 8"><rect width="11" height="8" fill="#ddd"/><path d="M0 0l5.5 4.5L11 0" stroke="#3a3a3a" fill="none"/></svg>info@northfieldpets-sample.com</li>
</ul></div>

<div class="abs bottom"></div>
<div class="abs copy">Copyrights © 2016, Northfield Pet Collective. All Rights Reserved.</div>
<div class="abs social"><span></span><span></span><span></span><span></span></div>
</body>
</html>
```